Web Site - Holloway-Strength.com

Design a 3 page web site for Holloway Strength. See attached design brief.
Holloway Strength - Web Site
www.holloway-strength.com

Design a 3 page web site for Holloway Strength, a small local fitness center that provided cardio and weights only (machines and free weights). There are no classes or other services offered at this facility. Holloway Strength is an affordable alternative to the big box, expensive fitness centers. It is small, local, convenient and a community oriented place to work out.
web site can be clean, simple and communicate basic information about the company and membership offers. Although the branding is black, orange and gray, the web site colors should be soft, light and neutral colors that will appeal to both men and women.
Text: Input generic text during design for each text area that will be modified later during the coding phase. The selected designer is expected to code the site and deliver all compressive files (images, files and code) for an unrestricted hand off and full ownership of all content by the client for future modifications by others.

Images
Images used can be generic royalty free images of people working out, on cardio machines, lifting on universal equipment, stretching or lifting weights or images with out people i.e a yoga mat, free weights, a row of cardio machines etc. This is an adults only facility - images can be a mix of men and women and of diverse multi ethnic backgrounds. Image of the actual gym are included below but should NOT be used on the web site.

Branding - See attached for vertical and horizontal logos for Holloway Strength. These can be used in any way and should be incorporated into the web site
WEB SITE OUTLINE
THREE web pages - Pages can be individual pages clicked through to each page from a navigation area but ALSO pages can be “blend together” into one long scrolling “home” or primary landing page.
1) Home Page with basic information
2) Membership Page (to be later integrated with Quillmark member software to show changing membership specials). - see example below - all text will change later
3) contact page - address - telephone number - google map directions
www.holloway-strength.com
Address:
Located in Tannery Brook Commons
418 E. Walnut Lane, Suite 305, Harlow Mills PA 19520
Tel: 484-555-0172

Target Market(s)

Men and Women - Adults over 18,

Industry/Entity Type

Fitness, Work Out, Gym

Coding

Coded - Design and coding required

Number of Pages Required

3 page

Requirements
Must have
• See Project Brief
Should not have
• Dark Colors that feel too masculine

```html
<!DOCTYPE html>
<html lang="en">
<head>
<meta charset="utf-8">
<title>Holloway Strength</title>
<link rel="stylesheet" href="https://fonts.googleapis.com/css2?family=Montserrat:wght@500;600;700;800&family=Open+Sans:wght@400;600&display=swap">
<style>
:root{
  --orange:#f26b1d;
  --ink:#1d1d1f;
  --text:#5a5a5a;
  --light:#f7f5f3;
  --line:#e6e2de;
  --white:#ffffff;
  --dark:#1a1a1a;
}
*{box-sizing:border-box;margin:0;padding:0}
html,body{width:1200px;height:2968px;overflow:hidden}
body{font-family:"Open Sans",Arial,sans-serif;color:var(--text);background:var(--white)}
h1,h2,h3,.nav,.btn,.brand{font-family:"Montserrat",Arial,sans-serif}

/* hero */
.hero{position:relative;height:690px;overflow:hidden}
.hero-photo{position:absolute;inset:0;background:linear-gradient(100deg,#3a2f2a 0%,#6b5d55 38%,#a89a90 62%,#5d524c 100%)}
.hero-shade{position:absolute;inset:0;background:linear-gradient(90deg,rgba(0,0,0,.55) 0%,rgba(0,0,0,.15) 55%,rgba(0,0,0,0) 100%)}
.site-header{position:absolute;top:0;left:0;right:0;height:90px;display:flex;align-items:center;padding:0 60px 0 150px}
.brand{display:flex;align-items:center;gap:12px;font-weight:800;font-size:22px;letter-spacing:.5px;color:var(--white);white-space:nowrap}
.brand-dot{width:30px;height:30px;border-radius:50%;background:var(--orange)}
.nav{display:flex;align-items:center;gap:34px;margin-left:150px;font-size:14px;font-weight:700;color:var(--white)}
.nav .active{background:var(--orange);padding:10px 20px;border-radius:4px}
.nav-phone{margin-left:auto;display:flex;align-items:center;gap:10px;font-family:"Montserrat",sans-serif;font-weight:700;font-size:18px;color:var(--white);white-space:nowrap}
.hero-copy{position:absolute;left:160px;top:175px}
.hero-copy h1{font-size:56px;line-height:62px;font-weight:800;text-transform:uppercase}
.hero-copy .o{color:var(--orange)}
.hero-copy .w{color:var(--white)}
.btn{display:inline-block;background:var(--orange);color:var(--white);font-weight:700;font-size:14px;letter-spacing:.5px;padding:18px 34px;border-radius:4px;text-transform:uppercase;white-space:nowrap}
.hero-copy .btn{margin-top:36px}

/* welcome */
.welcome{height:560px;display:flex;padding:0 120px 0 160px;align-items:center;gap:100px}
.welcome-mark{width:430px;height:340px;display:flex;flex-direction:column;align-items:center;justify-content:center;gap:26px;flex:none}
.welcome-mark .circle{width:220px;height:220px;border-radius:50%;background:var(--orange)}
.welcome-mark .name{font-family:"Montserrat",sans-serif;font-weight:800;font-size:30px;color:var(--ink);letter-spacing:1px;white-space:nowrap}
.welcome-text{width:400px}
.welcome-text .kicker{font-family:"Montserrat",sans-serif;font-weight:700;font-size:22px;color:var(--ink)}
.welcome-text h2{font-size:32px;font-weight:800;color:var(--ink);margin-top:2px;white-space:nowrap}
.welcome-text h2 span{color:var(--orange)}
.welcome-text p{font-size:14px;line-height:24px;margin-top:26px}
.ticks{list-style:none;margin-top:22px}
.ticks li{font-size:13px;line-height:26px;padding-left:22px;position:relative}
.ticks li::before{content:"";position:absolute;left:0;top:9px;width:9px;height:9px;border-radius:50%;background:var(--orange)}

/* membership */
.membership{height:690px;background:var(--light);border-top:1px solid var(--line);padding-top:58px}
.section-title{text-align:center;font-size:32px;font-weight:800;color:var(--ink)}
.section-title::after{content:"";display:block;width:60px;height:3px;background:var(--orange);margin:14px auto 0}
.plans{display:flex;gap:32px;justify-content:center;margin-top:60px}
.plan{position:relative;width:452px;height:432px;background:var(--white);border-radius:6px;box-shadow:0 10px 30px rgba(0,0,0,.08);padding:40px 34px}
.plan h3{font-size:22px;font-weight:700;color:var(--ink);width:300px}
.plan p{font-size:12.5px;line-height:20px;margin-top:14px}
.plan .note{font-weight:600;color:var(--ink)}
.price{position:absolute;top:-22px;right:-10px;width:100px;height:100px;border-radius:50%;background:var(--orange);color:var(--white);display:flex;flex-direction:column;align-items:center;justify-content:center;font-family:"Montserrat",sans-serif}
.price b{font-size:26px;font-weight:800;line-height:1}
.price small{font-size:11px;margin-top:4px}
.plan-actions{position:absolute;left:34px;bottom:30px;display:flex;flex-direction:column;gap:16px}
.plan-actions .btn{font-size:11px;padding:12px 20px;align-self:flex-start}
.btn-outline{font-family:"Montserrat",sans-serif;font-size:11px;font-weight:700;color:var(--ink);border:1.5px solid var(--ink);border-radius:4px;padding:11px 20px;display:flex;align-items:center;gap:14px;text-transform:uppercase;white-space:nowrap}

/* contact */
.contact{height:216px;display:flex;align-items:center;padding:0 120px 0 160px}
.contact-head{display:flex;align-items:center;gap:24px;width:500px;flex:none}
.contact-head .square{width:80px;height:80px;background:var(--orange);border-radius:6px;flex:none}
.contact-head h2{font-size:40px;font-weight:800;color:var(--ink);white-space:nowrap}
.contact-info h3{font-size:20px;font-weight:700;color:var(--ink);white-space:nowrap}
.contact-info address{font-style:normal;font-size:16px;margin-top:8px;white-space:nowrap}
.call{display:flex;align-items:center;gap:18px;margin-top:18px}
.call .btn{font-size:12px;padding:10px 18px;display:flex;align-items:center;gap:8px}
.call strong{font-family:"Montserrat",sans-serif;font-size:24px;color:var(--orange)}

/* map */
.map{height:420px;background:linear-gradient(135deg,#dcead6 0%,#eef1ea 40%,#f4f3ef 60%,#d7e8d2 100%)}

/* footer */
.site-footer{height:392px;background:var(--dark);display:flex;flex-direction:column;align-items:center;justify-content:center;color:var(--white)}
.site-footer .brand{font-size:30px;color:var(--white)}
.site-footer .brand-dot{width:40px;height:40px}
.footer-nav{display:flex;gap:40px;margin-top:48px;font-family:"Montserrat",sans-serif;font-weight:700;font-size:14px}
.copyright{margin-top:36px;font-size:12px;color:#bdbdbd}
</style>
</head>
<body>

<section class="hero">
  <div class="hero-photo" role="img" aria-label="Photo of members training on elliptical cardio machines in a bright gym"></div>
  <div class="hero-shade"></div>
  <header class="site-header">
    <div class="brand"><span class="brand-dot"></span>HOLLOWAY STRENGTH</div>
    <nav class="nav">
      <span class="active">HOME</span>
      <span>MEMBERSHIP</span>
      <span>CONTACT</span>
    </nav>
    <div class="nav-phone">
      <svg width="20" height="20" viewBox="0 0 24 24" fill="#fff"><path d="M6.6 10.8a15.1 15.1 0 0 0 6.6 6.6l2.2-2.2c.3-.3.7-.4 1-.2 1.1.4 2.3.6 3.6.6.6 0 1 .4 1 1V20c0 .6-.4 1-1 1C10.6 21 3 13.4 3 4c0-.6.4-1 1-1h3.5c.6 0 1 .4 1 1 0 1.3.2 2.5.6 3.6.1.3 0 .7-.2 1z"/></svg>
      484-555-0172
    </div>
  </header>
  <div class="hero-copy">
    <h1><span class="o">Stronger.</span><br><span class="o">Healthier.</span><br><span class="w">Closer to</span><br><span class="w">Home.</span></h1>
    <a class="btn">Contact Us</a>
  </div>
</section>

<section class="welcome">
  <div class="welcome-mark">
    <span class="circle"></span>
    <span class="name">HOLLOWAY STRENGTH</span>
  </div>
  <div class="welcome-text">
    <div class="kicker">WELCOME TO</div>
    <h2>HOLLOWAY <span>STRENGTH</span></h2>
    <p>We are a small, local gym built for people who want to train without the crowds or the high fees. Our floor offers cardio machines, strength machines and a full free weight area, open to adults who value a friendly, clean and welcoming place close to home. Stop by for a tour and meet our team of neighbors who love to lift and move every day.</p>
    <ul class="ticks">
      <li>Modern cardio machines with easy to use controls</li>
      <li>Free weights and racks for every training level</li>
      <li>Focus on fitness with no pricey extra fees</li>
      <li>Friendly staff who know members by name</li>
    </ul>
  </div>
</section>

<section class="membership">
  <h2 class="section-title">MEMBERSHIP</h2>
  <div class="plans">
    <article class="plan">
      <div class="price"><b>$199</b><small>/ month</small></div>
      <h3>Signature Membership</h3>
      <p>Includes our most popular amenities: full cardio floor, strength machines, free weight area, locker rooms and extended hours every day.</p>
      <p>Unlimited gym access, two guest passes each month, a fitness assessment and a custom starter plan with support from our floor staff.</p>
      <p>Access to the Tannery Brook location only.</p>
      <p class="note">Plus review exclusive new member benefits, see below for details.</p>
      <div class="plan-actions">
        <a class="btn">Select Membership</a>
        <span class="btn-outline">Additional membership details <svg width="18" height="10" viewBox="0 0 18 10"><path d="M0 5h16M12 1l4 4-4 4" stroke="#1d1d1f" stroke-width="1.5" fill="none"/></svg></span>
      </div>
    </article>
    <article class="plan">
      <div class="price"><b>$179</b><small>/ month</small></div>
      <h3>26 &amp; Under Membership</h3>
      <p>Discounted membership designed for members ages 18 to 26. Includes our most popular amenities: cardio floor, strength machines and free weights.</p>
      <p>Access to the Tannery Brook location only.</p>
      <p class="note">Eligibility Requirements</p>
      <p>Plus review exclusive new member benefits, see below for details.</p>
      <div class="plan-actions">
        <a class="btn">Select Membership</a>
        <span class="btn-outline">Additional membership details <svg width="18" height="10" viewBox="0 0 18 10"><path d="M0 5h16M12 1l4 4-4 4" stroke="#1d1d1f" stroke-width="1.5" fill="none"/></svg></span>
      </div>
    </article>
  </div>
</section>

<section class="contact">
  <div class="contact-head">
    <span class="square"></span>
    <h2>CONTACT US</h2>
  </div>
  <div class="contact-info">
    <h3>Located in Tannery Brook Commons</h3>
    <address>418 E. Walnut Lane, Suite 305, Harlow Mills PA 19520</address>
    <div class="call">
      <a class="btn"><svg width="14" height="14" viewBox="0 0 24 24" fill="#fff"><path d="M6.6 10.8a15.1 15.1 0 0 0 6.6 6.6l2.2-2.2c.3-.3.7-.4 1-.2 1.1.4 2.3.6 3.6.6.6 0 1 .4 1 1V20c0 .6-.4 1-1 1C10.6 21 3 13.4 3 4c0-.6.4-1 1-1h3.5c.6 0 1 .4 1 1 0 1.3.2 2.5.6 3.6.1.3 0 .7-.2 1z"/></svg>Call Us</a>
      <strong>484-555-0172</strong>
    </div>
  </div>
</section>

<div class="map" role="img" aria-label="Street map showing directions to the gym location"></div>

<footer class="site-footer">
  <div class="brand"><span class="brand-dot"></span>HOLLOWAY STRENGTH</div>
  <nav class="footer-nav"><span>HOME</span><span>MEMBERSHIP</span><span>CONTACT</span></nav>
  <p class="copyright">Copyright © 2024 All Rights Reserved</p>
</footer>

</body>
</html>
```